Financial Dashboard UI design

We are building a financial dashboard for business management teams, and would like a futuristic and sophisticated design (light and dark themes).

There are a total of 3 screens (attached images: nemo1, nemo2, nemo3).
nemo1 image is comprised of 6 scorecards (attached image: scorecard)
This will also need a design.

So, I'm expecting 4 UI designs in total.

I've added some example UI for inspiration. (sample1 , sample2, sample3, sample4).

Thanks

```html
<!DOCTYPE html>
<html lang="en">
<head>
<meta charset="utf-8">
<title>Financial Dashboard – Scorecards</title>
<link href="https://fonts.googleapis.com/css2?family=Roboto:wght@400;500;700&family=Titillium+Web:wght@600;700&display=swap" rel="stylesheet">
<style>
  :root{
    --page:#f7f7f9;
    --header:#ffffff;
    --search:#f4f4f7;
    --ink:#1b1b1f;
    --muted:#9a9aa3;
    --accent-purple:#6a1fd0;
    --badge-amber:#ffa41b;
    --unpaid:#82a6d3;
    --paid:#3e6ca6;
    --track:#ffffff;
    --target:#ee1c1c;
    --rate-blue:#3e6ca6;
    --dot-cyan:#4fc3f7;
    --dot-pink:#e0218a;
    --icon:#a4a7b0;
    --avatar:#cfcfd2;
  }
  *{box-sizing:border-box;margin:0;padding:0}
  html,body{width:1200px;height:725px;overflow:hidden}
  body{background:var(--page);font-family:"Roboto",sans-serif;color:var(--ink);position:relative}

  /* Top bar */
  .topbar{position:absolute;left:0;top:0;width:1200px;height:62px;background:var(--header)}
  .search{position:absolute;left:38px;top:14px;width:252px;height:34px;border-radius:17px;background:var(--search);display:flex;align-items:center;padding-left:18px;gap:10px;font-size:8px;color:var(--muted)}
  .tool{position:absolute;top:22px;width:16px;height:16px}
  .tool .count{position:absolute;left:7px;top:-7px;width:12px;height:12px;border-radius:50%;background:var(--dot-cyan);color:#fff;font-size:6.5px;display:flex;align-items:center;justify-content:center;font-weight:500}
  .tool .count.alert{background:var(--dot-pink)}
  .language{position:absolute;left:926px;top:14px;width:89px;height:34px;border:1px solid #eeeef2;border-radius:17px;display:flex;align-items:center;padding-left:9px;gap:6px;font-size:7.5px;font-weight:700}
  .avatar{position:absolute;left:1047px;top:16px;width:29px;height:29px;border-radius:6px;background:var(--avatar)}
  .user{position:absolute;left:1089px;top:20px;line-height:1}
  .user .name{font-size:7.5px;font-weight:700}
  .user .role{font-size:6.5px;color:var(--muted);margin-top:6px}
  .user-caret{position:absolute;left:1153px;top:28px}

  /* Scorecards */
  .card{position:absolute;width:196px;height:290px}
  .updated{position:absolute;left:6px;top:9px;font-size:8.5px}
  .amount{position:absolute;left:117px;top:5px;width:55px;height:15px;border-radius:8px;background:var(--badge-amber);color:#fff;font-size:8px;font-weight:700;display:flex;align-items:center;justify-content:center;letter-spacing:.2px}
  .title{position:absolute;left:0;top:30px;width:154px;height:34px;display:flex;align-items:center;justify-content:center;text-align:center;font-family:"Titillium Web",sans-serif;font-weight:700;font-size:11.5px;line-height:15px;letter-spacing:.3px}
  .budget{position:absolute;left:40px;top:68px;width:68px;text-align:center;font-size:12px;color:#333}
  .gauge{position:absolute;left:53px;top:93px;width:41px;height:180px;border-radius:8px;background:var(--track);overflow:hidden}
  .gauge i{position:absolute;left:0;bottom:0;width:100%;border-radius:8px}
  .gauge .fill-unpaid{height:var(--light);background:var(--unpaid)}
  .gauge .fill-paid{height:var(--dark);background:var(--paid)}
  .max{position:absolute;left:100px;top:83px;font-size:6px;font-weight:700}
  .scale{position:absolute;left:104px;top:100px;height:171px;list-style:none;display:flex;flex-direction:column;justify-content:space-between;font-size:5px;color:#333}
  .ytd{position:absolute;left:4px;font-size:6px;font-weight:700;line-height:12px}
  .pointer{position:absolute;left:0;top:0;width:196px;height:290px;pointer-events:none}
  .legend{position:absolute;left:0;font-size:6px;font-weight:700;line-height:12px;padding-left:13px}
  .legend::before{content:"";position:absolute;left:0;top:3px;width:6px;height:6px;border-radius:50%}
  .legend.unpaid{top:210px}
  .legend.unpaid::before{background:var(--unpaid)}
  .legend.paid{top:246px}
  .legend.paid::before{background:var(--paid)}
  .subrate{position:absolute;left:128px;top:158px;font-size:5px;font-weight:700;line-height:8px;text-align:center}
  .subrate b{display:block;color:var(--rate-blue)}
  .spark{position:absolute;left:130px;top:243px;width:42px;height:30px}
  .gauge.narrow{left:50px;width:21px}
  .track-target{position:absolute;left:77px;top:93px;width:22px;height:180px;border-radius:8px;background:var(--track)}
  .ytd.inside{left:74px;width:30px;text-align:center}
</style>
</head>
<body>

<header class="topbar">
  <div class="search">
    <svg width="14" height="14" viewBox="0 0 14 14"><circle cx="8" cy="6" r="4.6" fill="none" stroke="var(--accent-purple)" stroke-width="1.6"/><line x1="4.6" y1="9.4" x2="1.5" y2="12.5" stroke="var(--accent-purple)" stroke-width="1.6" stroke-linecap="round"/></svg>
    Search here
  </div>
  <div class="tool" style="left:778px">
    <svg width="16" height="16" viewBox="0 0 16 16"><path d="M3 12h10l-1.5-2V7a3.5 3.5 0 0 0-7 0v3z" fill="var(--icon)"/><circle cx="8" cy="13.5" r="1.4" fill="var(--icon)"/></svg>
    <span class="count">12</span>
  </div>
  <div class="tool" style="left:812px">
    <svg width="16" height="16" viewBox="0 0 16 16"><rect x="2" y="6" width="12" height="3" fill="var(--icon)"/><rect x="3" y="9.8" width="10" height="5" fill="var(--icon)"/><rect x="7.4" y="6" width="1.2" height="9" fill="#fff"/></svg>
    <span class="count">5</span>
  </div>
  <div class="tool" style="left:845px">
    <svg width="16" height="16" viewBox="0 0 16 16"><path d="M2 6a5 4 0 0 1 10 0 5 4 0 0 1-7 3.6L2 11l1-2.5A4 4 0 0 1 2 6z" fill="var(--icon)"/><path d="M6 11a5 4 0 0 0 8-1l1 3-3-1" fill="var(--icon)"/></svg>
    <span class="count">2</span>
  </div>
  <div class="tool" style="left:878px">
    <svg width="16" height="16" viewBox="0 0 16 16"><rect x="2" y="5" width="12" height="9" rx="1.5" fill="var(--icon)"/><rect x="5.5" y="3" width="5" height="3" rx="1" fill="none" stroke="var(--icon)" stroke-width="1.2"/></svg>
    <span class="count alert">!</span>
  </div>
  <div class="language">
    <svg width="15" height="15" viewBox="0 0 15 15" role="img" aria-label="Language flag">
      <clipPath id="flagClip"><circle cx="7.5" cy="7.5" r="7"/></clipPath>
      <g clip-path="url(#flagClip)">
        <rect width="15" height="15" fill="#fff"/>
        <rect y="0.5" width="15" height="2" fill="#d22"/><rect y="4.5" width="15" height="2" fill="#d22"/><rect y="8.5" width="15" height="2" fill="#d22"/><rect y="12.5" width="15" height="2" fill="#d22"/>
        <rect width="7" height="7" fill="#2b3f8f"/>
      </g>
    </svg>
    ENGLISH
    <svg width="8" height="5" viewBox="0 0 8 5" style="margin-left:6px"><path d="M0 0h8L4 5z" fill="var(--icon)"/></svg>
  </div>
  <div class="avatar"></div>
  <div class="user"><p class="name">Mara Lindqvist</p><p class="role">Super Admin</p></div>
  <svg class="user-caret" width="8" height="5" viewBox="0 0 8 5"><path d="M0 0h8L4 5z" fill="var(--icon)"/></svg>
</header>

<!-- Row 1 -->
<article class="card" style="left:24px;top:96px;--light:68%;--dark:46%">
  <p class="updated">Updated Jul 20</p><span class="amount">$ 217.75 k</span>
  <h2 class="title">FOUNDATION<br>CONTRIBUTIONS</h2>
  <p class="budget">Budget</p>
  <div class="gauge"><i class="fill-unpaid"></i><i class="fill-paid"></i></div>
  <span class="max">$4.51M</span>
  <ul class="scale"><li>90%</li><li>80%</li><li>70%</li><li>60%</li><li>50%</li><li>40%</li><li>30%</li><li>20%</li><li>10%</li><li>0%</li></ul>
  <p class="ytd" style="top:126px">ytd Target<br>$1.45M</p>
  <svg class="pointer"><line x1="36" y1="144" x2="80" y2="170" stroke="var(--target)" stroke-width="1.2"/><line x1="70" y1="170" x2="84" y2="170" stroke="var(--target)" stroke-width="1.2"/></svg>
  <p class="legend unpaid">Unpaid<br>$417.35k</p><p class="legend paid">Paid<br>$1.25M</p>
  <p class="subrate">Sub rate<b>77%</b></p>
  <svg class="spark" viewBox="0 0 42 30"><line x1="0" y1="12" x2="42" y2="12" stroke="#111" stroke-width="1"/><path d="M1 28C6 14 11 14 15 20S24 22 28 12S36 -2 40 5" fill="none" stroke="var(--accent-purple)" stroke-width="2.4" stroke-linecap="round"/></svg>
</article>

<article class="card" style="left:220px;top:96px;--light:47%;--dark:24%">
  <p class="updated">Updated Jul 20</p><span class="amount">$ 217.75 k</span>
  <h2 class="title">INDIVIDUAL<br>CONTRIBUTIONS</h2>
  <p class="budget">Budget</p>
  <div class="gauge"><i class="fill-unpaid"></i><i class="fill-paid"></i></div>
  <span class="max">$4.51M</span>
  <ul class="scale"><li>90%</li><li>80%</li><li>70%</li><li>60%</li><li>50%</li><li>40%</li><li>30%</li><li>20%</li><li>10%</li><li>0%</li></ul>
  <p class="ytd" style="top:154px">ytd Target<br>$1.45M</p>
  <svg class="pointer"><line x1="36" y1="172" x2="80" y2="201" stroke="var(--target)" stroke-width="1.2"/><line x1="70" y1="201" x2="84" y2="201" stroke="var(--target)" stroke-width="1.2"/></svg>
  <p class="legend unpaid">Unpaid<br>$417.35k</p><p class="legend paid">Paid<br>$1.25M</p>
  <p class="subrate">Sub rate<b>77%</b></p>
  <svg class="spark" viewBox="0 0 42 30"><line x1="0" y1="12" x2="42" y2="12" stroke="#111" stroke-width="1"/><path d="M1 28C6 14 11 14 15 20S24 22 28 12S36 -2 40 5" fill="none" stroke="var(--accent-purple)" stroke-width="2.4" stroke-linecap="round"/></svg>
</article>

<article class="card" style="left:416px;top:95px;--light:88%;--dark:58%">
  <p class="updated">Updated Jul 20</p><span class="amount">$ 217.75 k</span>
  <h2 class="title">BUSINESS<br>CONTRIBUTIONS</h2>
  <p class="budget">Budget</p>
  <div class="gauge"><i class="fill-unpaid"></i><i class="fill-paid"></i></div>
  <span class="max">$4.51M</span>
  <ul class="scale"><li>90%</li><li>80%</li><li>70%</li><li>60%</li><li>50%</li><li>40%</li><li>30%</li><li>20%</li><li>10%</li><li>0%</li></ul>
  <p class="ytd" style="top:120px">ytd Target<br>$1.45M</p>
  <svg class="pointer"><line x1="36" y1="138" x2="80" y2="161" stroke="var(--target)" stroke-width="1.2"/><line x1="70" y1="161" x2="84" y2="161" stroke="var(--target)" stroke-width="1.2"/></svg>
  <p class="legend unpaid">Unpaid<br>$417.35k</p><p class="legend paid">Paid<br>$1.25M</p>
  <p class="subrate">Sub rate<b>77%</b></p>
  <svg class="spark" viewBox="0 0 42 30"><line x1="0" y1="12" x2="42" y2="12" stroke="#111" stroke-width="1"/><path d="M1 28C6 14 11 14 15 20S24 22 28 12S36 -2 40 5" fill="none" stroke="var(--accent-purple)" stroke-width="2.4" stroke-linecap="round"/></svg>
</article>

<article class="card" style="left:612px;top:97px;--light:68%;--dark:46%">
  <p class="updated">Updated Jul 20</p><span class="amount">$ 217.75 k</span>
  <h2 class="title">GRANTS FROM<br>NATIONAL</h2>
  <p class="budget">Budget</p>
  <div class="gauge"><i class="fill-unpaid"></i><i class="fill-paid"></i></div>
  <span class="max">$4.51M</span>
  <ul class="scale"><li>90%</li><li>80%</li><li>70%</li><li>60%</li><li>50%</li><li>40%</li><li>30%</li><li>20%</li><li>10%</li><li>0%</li></ul>
  <p class="ytd" style="top:129px">ytd Target<br>$1.45M</p>
  <svg class="pointer"><line x1="36" y1="147" x2="80" y2="172" stroke="var(--target)" stroke-width="1.2"/><line x1="70" y1="172" x2="84" y2="172" stroke="var(--target)" stroke-width="1.2"/></svg>
  <p class="legend unpaid">Unpaid<br>$417.35k</p><p class="legend paid">Paid<br>$1.25M</p>
  <p class="subrate">Sub rate<b>77%</b></p>
  <svg class="spark" viewBox="0 0 42 30"><line x1="0" y1="12" x2="42" y2="12" stroke="#111" stroke-width="1"/><path d="M1 28C6 14 11 14 15 20S24 22 28 12S36 -2 40 5" fill="none" stroke="var(--accent-purple)" stroke-width="2.4" stroke-linecap="round"/></svg>
</article>

<article class="card" style="left:808px;top:98px;--light:83%;--dark:56%">
  <p class="updated">Updated Jul 20</p><span class="amount">$ 217.75 k</span>
  <h2 class="title">SPECIAL<br>EVENTS</h2>
  <p class="budget">Budget</p>
  <div class="gauge"><i class="fill-unpaid"></i><i class="fill-paid"></i></div>
  <span class="max">$4.51M</span>
  <ul class="scale"><li>90%</li><li>80%</li><li>70%</li><li>60%</li><li>50%</li><li>40%</li><li>30%</li><li>20%</li><li>10%</li><li>0%</li></ul>
  <p class="ytd" style="top:123px">ytd Target<br>$1.45M</p>
  <svg class="pointer"><line x1="36" y1="141" x2="80" y2="165" stroke="var(--target)" stroke-width="1.2"/><line x1="70" y1="165" x2="84" y2="165" stroke="var(--target)" stroke-width="1.2"/></svg>
  <p class="legend unpaid">Unpaid<br>$417.35k</p><p class="legend paid">Paid<br>$1.25M</p>
  <p class="subrate">Sub rate<b>77%</b></p>
  <svg class="spark" viewBox="0 0 42 30"><line x1="0" y1="12" x2="42" y2="12" stroke="#111" stroke-width="1"/><path d="M1 28C6 14 11 14 15 20S24 22 28 12S36 -2 40 5" fill="none" stroke="var(--accent-purple)" stroke-width="2.4" stroke-linecap="round"/></svg>
</article>

<article class="card" style="left:1004px;top:98px;--light:71%;--dark:35%">
  <p class="updated">Updated Jul 20</p><span class="amount">$ 217.75 k</span>
  <h2 class="title">OTHER<br>INCOME</h2>
  <p class="budget">Budget</p>
  <div class="gauge narrow"><i class="fill-unpaid"></i><i class="fill-paid"></i></div>
  <div class="track-target"></div>
  <span class="max">$4.51M</span>
  <ul class="scale"><li>90%</li><li>80%</li><li>70%</li><li>60%</li><li>50%</li><li>40%</li><li>30%</li><li>20%</li><li>10%</li><li>0%</li></ul>
  <p class="ytd inside" style="top:192px">ytd<br>Target<br>$1.45M</p>
  <svg class="pointer"><line x1="89" y1="230" x2="89" y2="248" stroke="var(--target)" stroke-width="1.2"/><line x1="83" y1="248" x2="95" y2="248" stroke="var(--target)" stroke-width="1.2"/></svg>
  <p class="legend unpaid">Unpaid<br>$417.35k</p><p class="legend paid">Paid<br>$1.25M</p>
  <p class="subrate">Sub rate<b>77%</b></p>
  <svg class="spark" viewBox="0 0 42 30"><line x1="0" y1="12" x2="42" y2="12" stroke="#111" stroke-width="1"/><path d="M1 28C6 14 11 14 15 20S24 22 28 12S36 -2 40 5" fill="none" stroke="var(--accent-purple)" stroke-width="2.4" stroke-linecap="round"/></svg>
</article>

<!-- Row 2 -->
<article class="card" style="left:21px;top:406px;--light:67%;--dark:33%">
  <p class="updated">Updated Jul 20</p><span class="amount">$ 217.75 k</span>
  <h2 class="title">NET ASSETS<br>RELEASED FROM...</h2>
  <p class="budget">Budget</p>
  <div class="gauge"><i class="fill-unpaid"></i><i class="fill-paid"></i></div>
  <span class="max">$4.51M</span>
  <ul class="scale"><li>90%</li><li>80%</li><li>70%</li><li>60%</li><li>50%</li><li>40%</li><li>30%</li><li>20%</li><li>10%</li><li>0%</li></ul>
  <p class="ytd" style="top:123px">ytd Target<br>$1.45M</p>
  <svg class="pointer"><line x1="36" y1="141" x2="80" y2="161" stroke="var(--target)" stroke-width="1.2"/><line x1="70" y1="161" x2="84" y2="161" stroke="var(--target)" stroke-width="1.2"/></svg>
  <p class="legend unpaid">Unpaid<br>$417.35k</p><p class="legend paid">Paid<br>$1.25M</p>
  <p class="subrate">Sub rate<b>77%</b></p>
  <svg class="spark" viewBox="0 0 42 30"><line x1="0" y1="12" x2="42" y2="12" stroke="#111" stroke-width="1"/><path d="M1 28C6 14 11 14 15 20S24 22 28 12S36 -2 40 5" fill="none" stroke="var(--accent-purple)" stroke-width="2.4" stroke-linecap="round"/></svg>
</article>

<article class="card" style="left:217px;top:408px;--light:88%;--dark:35%">
  <p class="updated">Updated Jul 20</p><span class="amount">$ 217.75 k</span>
  <h2 class="title">TOTAL<br>RECEIPTS</h2>
  <p class="budget">Budget</p>
  <div class="gauge"><i class="fill-unpaid"></i><i class="fill-paid"></i></div>
  <span class="max">$4.51M</span>
  <ul class="scale"><li>90%</li><li>80%</li><li>70%</li><li>60%</li><li>50%</li><li>40%</li><li>30%</li><li>20%</li><li>10%</li><li>0%</li></ul>
  <p class="ytd" style="top:132px">ytd Target<br>$1.45M</p>
  <svg class="pointer"><line x1="36" y1="150" x2="80" y2="167" stroke="var(--target)" stroke-width="1.2"/><line x1="70" y1="167" x2="84" y2="167" stroke="var(--target)" stroke-width="1.2"/></svg>
  <p class="legend unpaid">Unpaid<br>$417.35k</p><p class="legend paid">Paid<br>$1.25M</p>
  <p class="subrate">Sub rate<b>77%</b></p>
  <svg class="spark" viewBox="0 0 42 30"><line x1="0" y1="12" x2="42" y2="12" stroke="#111" stroke-width="1"/><path d="M1 28C6 14 11 14 15 20S24 22 28 12S36 -2 40 5" fill="none" stroke="var(--accent-purple)" stroke-width="2.4" stroke-linecap="round"/></svg>
</article>

<article class="card" style="left:413px;top:409px;--light:72%;--dark:36%">
  <p class="updated">Updated Jul 20</p><span class="amount">$ 217.75 k</span>
  <h2 class="title">SALARIES<br>AND WAGES</h2>
  <p class="budget">Budget</p>
  <div class="gauge"><i class="fill-unpaid"></i><i class="fill-paid"></i></div>
  <span class="max">$4.51M</span>
  <ul class="scale"><li>90%</li><li>80%</li><li>70%</li><li>60%</li><li>50%</li><li>40%</li><li>30%</li><li>20%</li><li>10%</li><li>0%</li></ul>
  <p class="ytd" style="top:149px">ytd Target<br>$1.45M</p>
  <svg class="pointer"><line x1="36" y1="167" x2="80" y2="187" stroke="var(--target)" stroke-width="1.2"/><line x1="70" y1="187" x2="84" y2="187" stroke="var(--target)" stroke-width="1.2"/></svg>
  <p class="legend unpaid">Unpaid<br>$417.35k</p><p class="legend paid">Paid<br>$1.25M</p>
  <p class="subrate">Sub rate<b>77%</b></p>
  <svg class="spark" viewBox="0 0 42 30"><line x1="0" y1="12" x2="42" y2="12" stroke="#111" stroke-width="1"/><path d="M1 28C6 14 11 14 15 20S24 22 28 12S36 -2 40 5" fill="none" stroke="var(--accent-purple)" stroke-width="2.4" stroke-linecap="round"/></svg>
</article>

<article class="card" style="left:609px;top:409px;--light:57%;--dark:26%">
  <p class="updated">Updated Jul 20</p><span class="amount">$ 217.75 k</span>
  <h2 class="title">PAYROLL<br>TAXES</h2>
  <p class="budget">Budget</p>
  <div class="gauge"><i class="fill-unpaid"></i><i class="fill-paid"></i></div>
  <span class="max">$4.51M</span>
  <ul class="scale"><li>90%</li><li>80%</li><li>70%</li><li>60%</li><li>50%</li><li>40%</li><li>30%</li><li>20%</li><li>10%</li><li>0%</li></ul>
  <p class="ytd" style="top:148px">ytd Target<br>$1.45M</p>
  <svg class="pointer"><line x1="36" y1="166" x2="80" y2="185" stroke="var(--target)" stroke-width="1.2"/><line x1="70" y1="185" x2="84" y2="185" stroke="var(--target)" stroke-width="1.2"/></svg>
  <p class="legend unpaid">Unpaid<br>$417.35k</p><p class="legend paid">Paid<br>$1.25M</p>
  <p class="subrate">Sub rate<b>77%</b></p>
  <svg class="spark" viewBox="0 0 42 30"><line x1="0" y1="12" x2="42" y2="12" stroke="#111" stroke-width="1"/><path d="M1 28C6 14 11 14 15 20S24 22 28 12S36 -2 40 5" fill="none" stroke="var(--accent-purple)" stroke-width="2.4" stroke-linecap="round"/></svg>
</article>

<article class="card" style="left:811px;top:408px;--light:67%;--dark:33%">
  <p class="updated">Updated Jul 20</p><span class="amount">$ 217.75 k</span>
  <h2 class="title">BENEFITS</h2>
  <p class="budget">Budget</p>
  <div class="gauge"><i class="fill-unpaid"></i><i class="fill-paid"></i></div>
  <span class="max">$4.51M</span>
  <ul class="scale"><li>90%</li><li>80%</li><li>70%</li><li>60%</li><li>50%</li><li>40%</li><li>30%</li><li>20%</li><li>10%</li><li>0%</li></ul>
  <p class="ytd" style="top:138px">ytd Target<br>$1.45M</p>
  <svg class="pointer"><line x1="36" y1="156" x2="80" y2="176" stroke="var(--target)" stroke-width="1.2"/><line x1="70" y1="176" x2="84" y2="176" stroke="var(--target)" stroke-width="1.2"/></svg>
  <p class="legend unpaid">Unpaid<br>$417.35k</p><p class="legend paid">Paid<br>$1.25M</p>
  <p class="subrate">Sub rate<b>77%</b></p>
  <svg class="spark" viewBox="0 0 42 30"><line x1="0" y1="12" x2="42" y2="12" stroke="#111" stroke-width="1"/><path d="M1 28C6 14 11 14 15 20S24 22 28 12S36 -2 40 5" fill="none" stroke="var(--accent-purple)" stroke-width="2.4" stroke-linecap="round"/></svg>
</article>

<article class="card" style="left:1007px;top:410px;--light:88%;--dark:35%">
  <p class="updated">Updated Jul 20</p><span class="amount">$ 217.75 k</span>
  <h2 class="title">OTHER<br>EXPENSES</h2>
  <p class="budget">Budget</p>
  <div class="gauge"><i class="fill-unpaid"></i><i class="fill-paid"></i></div>
  <span class="max">$4.51M</span>
  <ul class="scale"><li>90%</li><li>80%</li><li>70%</li><li>60%</li><li>50%</li><li>40%</li><li>30%</li><li>20%</li><li>10%</li><li>0%</li></ul>
  <p class="ytd" style="top:135px">ytd Target<br>$1.45M</p>
  <svg class="pointer"><line x1="36" y1="153" x2="80" y2="170" stroke="var(--target)" stroke-width="1.2"/><line x1="70" y1="170" x2="84" y2="170" stroke="var(--target)" stroke-width="1.2"/></svg>
  <p class="legend unpaid">Unpaid<br>$417.35k</p><p class="legend paid">Paid<br>$1.25M</p>
  <p class="subrate">Sub rate<b>77%</b></p>
  <svg class="spark" viewBox="0 0 42 30"><line x1="0" y1="12" x2="42" y2="12" stroke="#111" stroke-width="1"/><path d="M1 28C6 14 11 14 15 20S24 22 28 12S36 -2 40 5" fill="none" stroke="var(--accent-purple)" stroke-width="2.4" stroke-linecap="round"/></svg>
</article>

</body>
</html>
```